Financial Workshop for Hollister Wealth

Postcard to comply with RMPS. Invitation to workshop for 55+ senior community.
"Estate Conservation Strategies and Legacy Planning"
Building a sound and lasting retirement portfolio with a focus on growth and asset protection.
Developing investment objectives
Understanding risk adversity
Preserving assets
Conservative growth strategies for saving and investing
Planning for uncovered health care costs
Estate planning
Dale Whitford, Chartered Money Counselorâ„¢

add to the text (bullets) after Estate Planning (on same line) and Wealth Transfer Strategies Thank you Added Friday, October 13, 2017

Target Market(s)

Seniors

Industry/Entity Type

Financial

Font styles to use
Sans Serif

Colors

Designer to choose colors to be used in the design.

Requirements
Must have
• Logo
• Eye-catching images
• Easy to read geared for seniors
• Upscale professional look
• Afresh new look from previous samples sent.
Nice to have
• Something that stands out among the many postcard mail pieces they will get.
Should not have
• aside from logo/photo samples are an example of previous workshops and should not be reused.

```html
<!DOCTYPE html>
<html lang="en">
<head>
<meta charset="utf-8">
<title>Hollister Wealth – Workshop Postcard</title>
<link href="https://fonts.googleapis.com/css2?family=Source+Sans+3:wght@400;600;700&family=Arimo&display=swap" rel="stylesheet">
<style>
  :root{
    --backdrop:#fdf2d3;
    --paper:#ffffff;
    --navy:#2e2a86;
    --violet:#7a78bf;
    --photo-warm:#c9b8a4;
    --photo-cool:#e7e4de;
    --tan:#e2dad1; --tan-edge:#cdc3b7;
    --grey:#ececec; --grey-edge:#d2d2d2;
    --teal:#d9e9e7; --teal-edge:#bcd4d1;
    --green:#dcecdc; --green-edge:#c2d9c2;
  }
  *{margin:0;padding:0;box-sizing:border-box}
  html,body{width:1200px;height:960px;overflow:hidden;background:var(--backdrop)}
  body{font-family:"Source Sans 3",sans-serif;color:var(--navy);position:relative}
  .card{position:absolute;left:276px;width:649px;height:450px;background:var(--paper);overflow:hidden}
  .card--front{top:18px}
  .card--back{top:480px}
  .abs{position:absolute}

  .hero-photo{left:0;top:0;width:440px;height:300px;background:linear-gradient(135deg,var(--photo-cool) 0%,var(--photo-warm) 55%,#a89580 100%)}
  .brand{display:flex;align-items:center;gap:8px;font-weight:600;font-size:22px;letter-spacing:1.5px;color:var(--navy)}
  .brand-mark{width:14px;height:14px;border-radius:50%;background:var(--navy)}
  .brand-box{left:0;top:38px;width:224px;height:58px;background:rgba(255,255,255,.92);padding-left:30px}
  .front-title{right:23px;top:54px;text-align:right;font-weight:700;font-size:23px;line-height:24px}
  .intro{left:470px;top:238px;width:170px;font-size:9.6px;line-height:12px}
  .topics{left:478px;top:288px;width:160px;font-size:9.6px;line-height:12px;list-style:none}
  .topics li{position:relative;padding-left:9px}
  .topics li::before{content:"•";position:absolute;left:0}
  .event-title{left:22px;top:254px;width:200px;text-align:center;font-weight:700;font-size:11.5px;line-height:15px}
  .event-meta{left:50px;top:298px;font-size:9.6px;line-height:12px;display:grid;grid-template-columns:44px auto}
  .food{left:0;top:338px;width:314px;height:38px;background:var(--navy);border-radius:0 19px 19px 0;color:#fff;font-weight:600;font-size:9.3px;line-height:12px;padding:7px 0 0 26px}
  .food svg{position:absolute;right:14px;top:7px}
  .contact{left:36px;top:388px;font-weight:600;font-size:9.4px;line-height:12px}

  .back-brand{left:30px;top:52px}
  .back-title{left:32px;top:118px;font-weight:700;font-size:28px;line-height:29px;letter-spacing:-.3px}
  .back-sub{left:32px;top:184px;font-size:10.2px}
  .indicia{left:543px;top:28px;width:77px;height:78px;border:1.5px dashed #222;font-family:"Arimo",sans-serif;font-size:9.6px;line-height:12px;color:#111;text-align:center;padding-top:8px}
  .address{left:442px;top:124px;width:180px;height:51px;border:1.5px solid #111;font-family:"Arimo",sans-serif;font-size:12px;line-height:14px;color:#111;padding:13px 0 0 7px}
  .headshot{left:581px;top:206px;width:42px;height:59px;background:linear-gradient(180deg,#a8a8a8,#55596a);border:2px solid #ddd}
  .presenter{right:16px;top:270px;font-weight:700;font-size:12.6px}
  .date-bar{left:345px;top:288px;width:304px;height:22px;background:var(--navy);color:#fff;font-size:12.4px;line-height:22px;text-align:center;border-radius:0 0 0 4px}
  .topic{position:absolute;border-radius:50%;border:3px solid;display:flex;align-items:center;justify-content:center;text-align:center;font-size:11.6px;line-height:14px;color:var(--navy)}
  .t-tan{background:var(--tan);border-color:var(--tan-edge)}
  .t-grey{background:var(--grey);border-color:var(--grey-edge)}
  .t-teal{background:var(--teal);border-color:var(--teal-edge)}
  .t-green{background:var(--green);border-color:var(--green-edge)}
</style>
</head>
<body>

<section class="card card--front">
  <div class="abs hero-photo" role="img" aria-label="Photo of a smiling senior couple looking at a tablet together over coffee"></div>
  <div class="abs brand-box brand"><span class="brand-mark"></span>HOLLISTER WEALTH</div>
  <svg class="abs" style="left:0;top:0" width="649" height="450" viewBox="0 0 649 450">
    <path d="M0 300 L0 275 C50 240 95 220 140 222 C230 226 300 300 440 300 L440 450 L0 450 Z" fill="var(--paper)"/>
    <path d="M0 275 C50 240 95 220 140 222 C230 226 300 300 440 300 L440 310 C300 312 230 240 140 236 C95 234 50 250 0 290 Z" fill="var(--violet)"/>
    <path d="M440 238 C500 208 580 200 649 232" fill="none" stroke="var(--violet)" stroke-width="5"/>
  </svg>
  <h1 class="abs front-title">Estate<br>Conservation<br>Strategies<br>and<br>Legacy Planning</h1>
  <p class="abs intro">Building a sound and lasting retirement portfolio with a focus on growth and income</p>
  <ul class="abs topics">
    <li>Developing Investment Objectives</li>
    <li>Understanding Risk Adversity</li>
    <li>Preserving Assets</li>
    <li>Conservative Growth Strategies for Saving and Investing</li>
    <li>Planning for Uncovered Healthcare Costs</li>
    <li>Estate Planning</li>
    <li>Wealth Transfer</li>
  </ul>
  <h2 class="abs event-title">Estate Conservation<br>Strategies and Legacy Planning</h2>
  <div class="abs event-meta"><span>When:</span><span>November 7th at 6:30 PM</span><span>Where:</span><span>Larkspur Hall</span></div>
  <div class="abs food">Gourmet Deli Sandwiches, Fresh fruit, Cheese cake and<br>Refreshments will be provided
    <svg width="28" height="24" viewBox="0 0 28 24"><rect x="0" y="11" width="13" height="3" rx="1.5" fill="#fff"/><rect x="0" y="16" width="13" height="3" rx="1.5" fill="#fff"/><path d="M1 9 Q6.5 3 12 9 Z" fill="#fff"/><path d="M15 6 L25 6 L23 23 L17 23 Z" fill="#fff"/><path d="M21 6 L24 0" stroke="#fff" stroke-width="1.5"/></svg>
  </div>
  <p class="abs contact">418 Brambleton Oaks Road, Cary, NC 27511<br>Phone: 919-555-0148</p>
</section>

<section class="card card--back">
  <div class="abs back-brand brand"><span class="brand-mark"></span>HOLLISTER WEALTH</div>
  <h1 class="abs back-title">Estate Conservation Strategies<br>and Legacy Planning</h1>
  <p class="abs back-sub">Building a sound and lasting retirement portfolio with a focus on growth and income</p>
  <div class="abs indicia">PRSRT STD<br>ECRWSS<br>U.S. POSTAGE<br>PAID<br>RMPS RETAIL</div>
  <div class="abs address">Local<br>Postal Customer</div>
  <svg class="abs" style="left:0;top:0" width="649" height="450" viewBox="0 0 649 450">
    <path d="M0 276 C40 240 90 222 140 222 C220 222 290 262 348 285 L348 291 C290 272 220 238 140 238 C90 238 40 256 0 292 Z" fill="var(--violet)"/>
    <path d="M540 266 C580 250 620 228 649 190" fill="none" stroke="var(--violet)" stroke-width="3"/>
  </svg>
  <div class="abs headshot" role="img" aria-label="Headshot portrait of the presenter"></div>
  <p class="abs presenter">Dale Whitford, Chartered Money Counselor™</p>
  <div class="abs date-bar">November 7th at 6:30 PM @ Larkspur Hall</div>

  <div class="topic t-tan" style="left:58px;top:234px;width:132px;height:132px;align-items:flex-start;padding-top:38px">Conservative Growth<br>Strategies for<br>Saving and Investing</div>
  <div class="topic t-grey" style="left:36px;top:324px;width:92px;height:92px">Understanding<br>Risk Adversity</div>
  <div class="topic t-teal" style="left:132px;top:330px;width:88px;height:88px">Estate<br>Planning</div>
  <div class="topic t-green" style="left:225px;top:330px;width:88px;height:88px">Wealth<br>Transfer</div>
  <div class="topic t-tan" style="left:318px;top:329px;width:88px;height:88px">Developing<br>Investment<br>Objectives</div>
  <div class="topic t-green" style="left:413px;top:329px;width:88px;height:88px">Preserving<br>Assets</div>
  <div class="topic t-teal" style="left:509px;top:321px;width:104px;height:104px">Planning for<br>Uncovered<br>Healthcare Costs</div>
</section>

</body>
</html>
```